Facebook, Twitter and Linkedin cover image design

Looking to update the facebook, twitter and aLinkedin cover images for Tandem Accounts . website www.tandacct.example
https://www.prolinknet.example/company/tandem-accounts-llc/mycompany/?viewAsMember=true
https://www.socialpage.example/tandacct
https://chirpline.example/tandacct

```html
<!DOCTYPE html>
<html lang="en">
<head>
<meta charset="utf-8">
<title>Tandem Accounts – Social Cover Set</title>
<link href="https://fonts.googleapis.com/css2?family=Roboto:wght@500;700&family=Montserrat:wght@400;500&display=swap" rel="stylesheet">
<style>
  :root {
    --board: #a9aaae;
    --label: #e4e5e8;
    --ink: #0b0b0b;
    --photo-dark: #151515;
    --photo-mid: #2e2e2e;
    --green: #4cb847;
    --green-deep: #2f8f2f;
    --white: #ffffff;
    --logo-grey: #6f6f6f;
  }
  * { box-sizing: border-box; margin: 0; padding: 0; }
  html, body { width: 1200px; height: 1180px; overflow: hidden; }
  body { background: var(--board); position: relative; font-family: "Roboto", Arial, sans-serif; }

  .board-label { position: absolute; left: 99px; color: var(--label); font: 400 16px "Roboto", Arial, sans-serif; }

  .cover { position: absolute; left: 99px; background: var(--ink); box-shadow: 0 4px 10px rgba(0,0,0,.35); }
  .cover-photo { position: absolute; inset: 0; overflow: hidden;
    background: linear-gradient(100deg, var(--ink) 0%, var(--photo-dark) 30%, var(--photo-mid) 65%, var(--photo-dark) 100%); }
  .cover-splash { position: absolute; right: 0; bottom: 0; width: 27%; height: 80%;
    background: radial-gradient(ellipse at 100% 100%, var(--green) 0%, var(--green) 38%, rgba(76,184,71,.55) 58%, rgba(76,184,71,0) 75%); }

  .brand { position: absolute; display: flex; align-items: center; gap: .35em; }
  .brand-mark { width: 2.6em; height: 2.6em; background: var(--green); flex: none; }
  .brand-name { color: var(--logo-grey); font-weight: 700; text-transform: uppercase; line-height: .95; font-size: 1em; }

  .partner { position: absolute; display: flex; align-items: center; gap: .35em; }
  .partner-mark { width: 1.5em; height: 1.5em; background: var(--green-deep); flex: none; }
  .partner-name { color: var(--logo-grey); font-weight: 500; font-size: 1.15em; }

  .pitch { position: absolute; left: 0; right: 0; text-align: center; color: var(--white); }
  .pitch-question { font-weight: 500; line-height: 1.2; }
  .pitch-offer { color: var(--green); font-weight: 700; line-height: 1.3; }
  .pitch-perks { font-family: "Montserrat", Arial, sans-serif; font-weight: 400; line-height: 1.5; list-style: none; }
  .pitch-perks li span::before { content: "•"; color: var(--green); font-size: 1.1em; margin: 0 .3em 0 .6em; }
  .pitch-url { display: flex; align-items: center; justify-content: center; margin-top: .6em; }
  .pitch-url::before, .pitch-url::after { content: ""; height: 1px; background: var(--green); }
  .pitch-url a { color: var(--white); text-decoration: none; background: var(--green); font-family: "Montserrat", Arial, sans-serif; letter-spacing: .35em; padding: .2em .8em .2em 1.1em; border-radius: .35em; }

  .avatar { position: absolute; border-radius: 50%; background: var(--white); border: 3px solid var(--white); box-shadow: 0 4px 10px rgba(0,0,0,.35), inset 0 0 0 2px var(--white), inset 0 0 0 3px var(--green-deep); display: flex; align-items: center; justify-content: center; }
  .avatar .brand { position: static; }

  /* Twitter */
  .cover--twitter { top: 69px; width: 951px; height: 317px; }
  .cover--twitter .brand-lead { left: 23px; top: 16px; font-size: 16px; }
  .cover--twitter .partner { right: 16px; top: 18px; font-size: 14px; }
  .cover--twitter .pitch { top: 55px; }
  .cover--twitter .pitch-question { font-size: 25px; }
  .cover--twitter .pitch-offer { font-size: 37px; }
  .cover--twitter .pitch-perks { font-size: 13.5px; }
  .cover--twitter .pitch-url a { font-size: 14px; }
  .cover--twitter .pitch-url::before, .cover--twitter .pitch-url::after { width: 55px; }
  .cover--twitter .avatar { left: 63px; top: 228px; width: 152px; height: 152px; font-size: 13px; }

  /* LinkedIn */
  .cover--linkedin { top: 511px; width: 1005px; height: 251px; }
  .cover--linkedin .brand-lead { left: 26px; top: 19px; font-size: 15px; }
  .cover--linkedin .partner { right: 25px; top: 14px; font-size: 14px; }
  .cover--linkedin .pitch { top: 40px; }
  .cover--linkedin .pitch-question { font-size: 22px; }
  .cover--linkedin .pitch-offer { font-size: 32px; }
  .cover--linkedin .pitch-perks { font-size: 12px; line-height: 1.4; }
  .cover--linkedin .pitch-url { margin-top: .4em; }
  .cover--linkedin .pitch-url a { font-size: 12.5px; }
  .cover--linkedin .pitch-url::before, .cover--linkedin .pitch-url::after { width: 105px; }
  .cover--linkedin .avatar { left: 74px; top: 175px; width: 152px; height: 152px; font-size: 13px; }

  /* Facebook */
  .cover--facebook { top: 902px; width: 540px; height: 200px; }
  .cover--facebook .brand-lead { left: 12px; top: 10px; font-size: 10px; }
  .cover--facebook .partner { right: 10px; top: 9px; font-size: 10px; }
  .cover--facebook .pitch { top: 38px; }
  .cover--facebook .pitch-question { font-size: 15px; }
  .cover--facebook .pitch-offer { font-size: 22px; }
  .cover--facebook .pitch-perks { font-size: 7.5px; line-height: 1.4; }
  .cover--facebook .pitch-url { margin-top: .4em; }
  .cover--facebook .pitch-url a { font-size: 8px; }
  .cover--facebook .pitch-url::before, .cover--facebook .pitch-url::after { width: 32px; }
  .cover--facebook .avatar { left: 30px; top: 135px; width: 106px; height: 106px; font-size: 9px; }
</style>
</head>
<body>

<p class="board-label" style="top:36px">Twitter Cover</p>
<section class="cover cover--twitter">
  <div class="cover-photo" role="img" aria-label="Darkened photo of a desk with a laptop showing an invoice and a calculator"></div>
  <div class="cover-splash" role="img" aria-label="Green paint splash decoration"></div>
  <div class="brand brand-lead"><span class="brand-mark"></span><span class="brand-name">Tandem<br>Accounts</span></div>
  <div class="partner"><span class="partner-mark"></span><span class="partner-name">Fleetpass</span></div>
  <div class="pitch">
    <h2 class="pitch-question">Are You Tired Of<br>Banking Your Customers?</h2>
    <h1 class="pitch-offer">Get Fast Invoice Payments!</h1>
    <ul class="pitch-perks">
      <li><span>Low Fixed Fees</span><span>No Contract Period</span></li>
      <li><span>Same Day Funding</span><span>Credit and Collection Management</span></li>
      <li><span>24/7 Online Monitoring</span><span>And Much More!</span></li>
    </ul>
    <div class="pitch-url"><a href="https://www.tandacct.example">www.tandacct.example</a></div>
  </div>
  <div class="avatar"><div class="brand"><span class="brand-mark"></span><span class="brand-name">Tandem<br>Accounts</span></div></div>
</section>

<p class="board-label" style="top:486px">Linkedin Cover</p>
<section class="cover cover--linkedin">
  <div class="cover-photo" role="img" aria-label="Darkened photo of a desk with a laptop showing an invoice and a calculator"></div>
  <div class="cover-splash" role="img" aria-label="Green paint splash decoration"></div>
  <div class="brand brand-lead"><span class="brand-mark"></span><span class="brand-name">Tandem<br>Accounts</span></div>
  <div class="partner"><span class="partner-mark"></span><span class="partner-name">Fleetpass</span></div>
  <div class="pitch">
    <h2 class="pitch-question">Are You Tired Of<br>Banking Your Customers?</h2>
    <h1 class="pitch-offer">Get Fast Invoice Payments!</h1>
    <ul class="pitch-perks">
      <li><span>Low Fixed Fees</span><span>No Contract Period</span></li>
      <li><span>Same Day Funding</span><span>Credit and Collection Management</span></li>
      <li><span>24/7 Online Monitoring</span><span>And Much More!</span></li>
    </ul>
    <div class="pitch-url"><a href="https://www.tandacct.example">www.tandacct.example</a></div>
  </div>
  <div class="avatar"><div class="brand"><span class="brand-mark"></span><span class="brand-name">Tandem<br>Accounts</span></div></div>
</section>

<p class="board-label" style="top:874px">Facebook Cover</p>
<section class="cover cover--facebook">
  <div class="cover-photo" role="img" aria-label="Darkened photo of a desk with a laptop showing an invoice and a calculator"></div>
  <div class="cover-splash" role="img" aria-label="Green paint splash decoration"></div>
  <div class="brand brand-lead"><span class="brand-mark"></span><span class="brand-name">Tandem<br>Accounts</span></div>
  <div class="partner"><span class="partner-mark"></span><span class="partner-name">Fleetpass</span></div>
  <div class="pitch">
    <h2 class="pitch-question">Are You Tired Of<br>Banking Your Customers?</h2>
    <h1 class="pitch-offer">Get Fast Invoice Payments!</h1>
    <ul class="pitch-perks">
      <li><span>Low Fixed Fees</span><span>No Contract Period</span></li>
      <li><span>Same Day Funding</span><span>Credit and Collection Management</span></li>
      <li><span>24/7 Online Monitoring</span><span>And Much More!</span></li>
    </ul>
    <div class="pitch-url"><a href="https://www.tandacct.example">www.tandacct.example</a></div>
  </div>
  <div class="avatar"><div class="brand"><span class="brand-mark"></span><span class="brand-name">Tandem<br>Accounts</span></div></div>
</section>

</body>
</html>
```